Quarvelon stickers design for our main topics (for example: agile and Kanban)

We are looking for sticker design, that will reflect our cooperate identity and can be used for the different topics in our company. We would like to start with our Agile Coaching Offers with a Kanban Sticker saying "stop starting, start finishing", A bad example can be find in the file upload ;)
Check out our homepage to get a feeling for the cooperate identity (www.quarvelon-beispiel.ch)

Target Market(s)

Customers and trainees from our trainings

Industry/Entity Type

Consulting

Colors
0355a3
fbed22

Requirements
Must have
• a cool design thats fits to our customer design
the 2 lines can be changed for future stickers ... like in the example "stop starting, start finishing" and "we show you how"
Nice to have
• -
Should not have
• -

```html
<!DOCTYPE html>
<html lang="en">
<head>
<meta charset="utf-8">
<title>Quarvelon Sticker – Stop starting, Start finishing</title>
<link rel="stylesheet" href="https://fonts.googleapis.com/css2?family=Roboto+Condensed:wght@400;700&family=Open+Sans:ital,wght@0,400;1,400&display=swap">
<style>
  :root {
    --brand-blue: #0336e6;
    --brand-yellow: #ece96f;
    --sticker-white: #ffffff;
    --ink-dark: #1c1c1c;
    --page-bg: #eeeeec;
  }
  html, body {
    margin: 0;
    padding: 0;
    width: 1200px;
    height: 718px;
    overflow: hidden;
    background: var(--page-bg);
  }
  .canvas {
    position: relative;
    width: 1200px;
    height: 718px;
  }
  .sticker {
    position: absolute;
    left: 50px;
    top: 216px;
    width: 1100px;
    height: 285px;
    filter: drop-shadow(3px 4px 5px rgba(0,0,0,0.25));
  }
  .sticker-base { fill: var(--sticker-white); }
  .band-blue { fill: var(--brand-blue); }
  .band-yellow { fill: var(--brand-yellow); }
  .checkbox-frame { fill: none; stroke: var(--brand-blue); stroke-width: 3; }
  .checkmark { fill: var(--brand-blue); }
  .headline-top {
    font-family: "Roboto Condensed", sans-serif;
    font-weight: 400;
    font-size: 38px;
    fill: var(--sticker-white);
  }
  .headline-bottom {
    font-family: "Roboto Condensed", sans-serif;
    font-weight: 700;
    font-size: 38px;
    fill: var(--brand-blue);
  }
  .tagline {
    font-family: "Open Sans", sans-serif;
    font-style: italic;
    font-size: 19px;
    fill: var(--ink-dark);
  }
  .company-name {
    font-family: "Open Sans", sans-serif;
    font-weight: 400;
    font-size: 20px;
    fill: var(--ink-dark);
  }
  .company-square { fill: var(--brand-blue); }
</style>
</head>
<body>
<main class="canvas">
  <svg class="sticker" viewBox="0 0 656 170" xmlns="http://www.w3.org/2000/svg" aria-label="Sticker: Stop starting, Start finishing – We show you how – quarvelon ag">
    <defs>
      <clipPath id="sticker-shape">
        <rect x="0" y="0" width="656" height="170" rx="11" ry="11"/>
      </clipPath>
    </defs>
    <rect class="sticker-base" x="0" y="0" width="656" height="170" rx="11" ry="11"/>
    <g clip-path="url(#sticker-shape)">
      <polygon class="band-blue" points="43,0 345,0 416,85 118,85"/>
      <polygon class="band-yellow" points="118,85 446,85 418,127 446,170 88,170"/>
    </g>

    <rect class="checkbox-frame" x="22" y="69" width="52" height="52"/>
    <path class="checkmark" d="M30 95 L38 91 L46 103 L82 77 L86 84 L46 112 Z"/>

    <text class="headline-top" x="228" y="59" text-anchor="middle">Stop starting,</text>
    <text class="headline-bottom" x="268" y="141" text-anchor="middle">Start finishing</text>

    <text class="tagline" x="620" y="76" text-anchor="end">We show you how</text>

    <rect class="company-square" x="470" y="104" width="26" height="26"/>
    <text class="company-name" x="506" y="124">quarvelon ag</text>
  </svg>
</main>
</body>
</html>
```